Visualization of a corporate strategy on 1 page

Hi, I need 1 page (a drawing/illustration) that depicts the ambition and strategy of a company. See attached my draft. Pleaes make it look like a hand drawing. It should be catchy. Not too many colors. The street depicts the road from today until 2020. If you have any questions, please get back to me. I will let you know more details. Make a first draft and I give you my input!

Industry/Entity Type

It Company

Font styles to use
Other font styles liked:
• Script style

Colors
0355a3
3176b5
33a6d7
1f9ad1
85cae6

Requirements
Must have
• Im open, please make a suggestion - it needs to look nice and memorable... that is the most important. The end product should look like a handwritten drawing rather than a digitial illustration

```html
<!DOCTYPE html>
<html lang="en">
<head>
<meta charset="utf-8">
<title>Halvorsen Strategy 2020</title>
<link href="https://fonts.googleapis.com/css2?family=Amatic+SC:wght@400;700&family=Dancing+Script:wght@400;600&display=swap" rel="stylesheet">
<style>
  :root {
    --sea: #c6e4ea;
    --land: #f5f3ec;
    --road: #9a9a9a;
    --flag: #45b3c9;
    --flag-light: #e9f6f9;
    --ink: #0d4f8f;
    --ink-soft: #3176b5;
    --line: #2c7ea6;
    --outline: #33a6d7;
    --shadow: #d4d4d4;
  }
  html, body { margin: 0; padding: 0; overflow: hidden; background: var(--sea); }
  .canvas { display: block; width: 1200px; height: 803px; }
  .caps { font-family: "Amatic SC", "Comic Sans MS", cursive; font-weight: 700; fill: var(--ink); }
  .script { font-family: "Dancing Script", "Brush Script MT", cursive; fill: var(--ink); }
  .step-number { font-family: "Dancing Script", cursive; fill: var(--outline); font-size: 24px; }
  .step-ring { fill: none; stroke: var(--outline); stroke-width: 2; }
  .flag { fill: var(--flag); stroke: var(--line); stroke-width: 2; }
  .flag-stitch { fill: none; stroke: var(--ink); stroke-width: 1.3; stroke-dasharray: 5 4; }
  .flag-light { fill: var(--flag-light); stroke: var(--outline); stroke-width: 2; }
  .pole { stroke: var(--ink-soft); stroke-width: 2.5; }
  .road { fill: none; stroke: var(--road); stroke-width: 24; stroke-linecap: round; stroke-linejoin: round; }
  .road-marks { fill: none; stroke: #fff; stroke-width: 2.5; stroke-dasharray: 14 11; }
  .placeholder { fill: #cfdbe6; }
  .chart-axis { stroke: var(--ink-soft); stroke-width: 1.5; fill: none; }
  .chart-bar { fill: #8fb3d6; stroke: var(--ink-soft); stroke-width: 1.2; }
  .checklist { fill: #fff; stroke: var(--ink-soft); stroke-width: 1.5; }
  .tick { fill: none; stroke: var(--ink-soft); stroke-width: 2; stroke-linecap: round; }
</style>
</head>
<body>
<svg class="canvas" viewBox="0 0 1200 803" xmlns="http://www.w3.org/2000/svg">
  <rect width="1200" height="803" fill="var(--sea)"/>

  <!-- land -->
  <path class="land" fill="var(--land)" d="M60 640 C40 540 150 520 150 480 C150 430 60 410 75 330 C90 230 60 140 200 128 C400 118 600 160 860 150 C1010 145 1080 120 1120 200 C1160 300 1100 380 1120 480 C1140 580 1010 620 965 700 C930 760 700 742 500 746 C300 750 90 770 60 640Z"/>

  <!-- road -->
  <path class="road" d="M188 712 C130 640 60 555 200 540 L850 548 C1010 550 1010 368 850 362 L220 345 C70 340 85 240 240 240 L700 226 C900 216 960 172 1050 152"/>
  <path class="road-marks" d="M188 712 C130 640 60 555 200 540 L850 548 C1010 550 1010 368 850 362 L220 345 C70 340 85 240 240 240 L700 226 C900 216 960 172 1050 152"/>

  <!-- title pocket -->
  <g class="title">
    <path class="flag" d="M472 -2 H722 V112 L597 158 L472 112Z"/>
    <path class="flag-stitch" d="M482 -2 V106 L597 148 L712 106 V-2"/>
    <text class="caps" x="597" y="38" text-anchor="middle" font-size="40" fill="#fff" style="fill:#fff">HALVORSEN</text>
    <text class="caps" x="597" y="80" text-anchor="middle" font-size="40" style="fill:#fff">STRATEGY</text>
    <text class="caps" x="597" y="122" text-anchor="middle" font-size="40" style="fill:#fff">2020</text>
  </g>

  <!-- goal ribbon -->
  <g class="goal">
    <line class="pole" x1="1140" y1="0" x2="1140" y2="20"/>
    <line class="pole" x1="1145" y1="20" x2="1200" y2="20"/>
    <path class="flag" d="M1043 -2 H1145 V178 L1094 148 L1043 178Z"/>
    <path class="flag-stitch" d="M1051 -2 V164 L1094 138 L1137 164 V-2"/>
    <text class="script" x="1078" y="45" font-size="20" style="fill:#fff">+20</text>
    <text class="script" x="1068" y="68" font-size="20" style="fill:#fff">m by</text>
    <text class="caps" x="1094" y="118" text-anchor="middle" font-size="50" style="fill:#fff">2020</text>
  </g>

  <!-- Veltrania -->
  <line class="pole" x1="70" y1="0" x2="70" y2="112"/>
  <path class="flag" d="M60 20 H215 L195 50 L215 80 H60Z"/>
  <path class="flag-stitch" d="M66 26 H204 L187 50 L204 74 H66"/>
  <text class="caps" x="126" y="66" text-anchor="middle" font-size="38">VELTRANIA</text>

  <rect class="placeholder" x="192" y="48" width="270" height="170" rx="30" role="img" aria-label="Drawing of a city skyline with office towers"/>

  <!-- Regrowth -->
  <line class="pole" x1="641" y1="232" x2="641" y2="346"/>
  <path class="flag" d="M628 256 H785 L765 285 L785 315 H628Z"/>
  <path class="flag-stitch" d="M634 262 H774 L757 285 L774 309 H634"/>
  <text class="caps" x="700" y="300" text-anchor="middle" font-size="38">REGROWTH</text>

  <!-- Services -->
  <line class="pole" x1="592" y1="372" x2="592" y2="488"/>
  <path class="flag" d="M580 396 H740 L720 425 L740 455 H580Z"/>
  <path class="flag-stitch" d="M586 402 H729 L712 425 L729 449 H586"/>
  <text class="caps" x="652" y="441" text-anchor="middle" font-size="40">SERVICES</text>

  <rect class="placeholder" x="375" y="385" width="150" height="140" rx="20" role="img" aria-label="Drawing of two business people shaking hands"/>
  <rect class="placeholder" x="762" y="388" width="118" height="136" rx="20" role="img" aria-label="Drawing of a factory with smoke"/>
  <rect class="placeholder" x="95" y="368" width="72" height="68" rx="20" role="img" aria-label="Drawing of two gears"/>
  <text class="script" x="180" y="428" font-size="19">operational</text>
  <text class="script" x="180" y="450" font-size="19">improvementa</text>

  <!-- Introducing new technologies -->
  <rect class="placeholder" x="1012" y="266" width="56" height="62" rx="25" role="img" aria-label="Speech bubble with an exclamation mark"/>
  <line class="pole" x1="988" y1="312" x2="988" y2="440"/>
  <path class="flag-light" d="M970 336 H1175 L1152 372 L1175 408 H970Z"/>
  <path class="flag-stitch" d="M976 342 H1162 L1144 372 L1162 402 H976" style="stroke:var(--outline)"/>
  <text class="script" x="990" y="367" font-size="20">Introducing</text>
  <text class="script" x="990" y="391" font-size="20">new technologies</text>

  <!-- Today -->
  <line class="pole" x1="225" y1="558" x2="225" y2="710"/>
  <path class="flag" d="M212 580 H370 L350 610 L370 640 H212Z"/>
  <path class="flag-stitch" d="M218 586 H359 L342 610 L359 634 H218"/>
  <text class="caps" x="282" y="627" text-anchor="middle" font-size="42">TODAY</text>
  <path class="flag-light" d="M228 655 H390 L372 672 L390 690 H228Z"/>
  <text class="script" x="236" y="681" font-size="20">Hous rules</text>

  <!-- checklist -->
  <g class="checklist-card">
    <rect class="checklist" x="408" y="598" width="88" height="74" rx="3"/>
    <path class="tick" d="M420 614 l5 5 l9 -10 M420 634 l5 5 l9 -10 M420 654 l5 5 l9 -10"/>
    <path class="tick" d="M442 614 H486 M442 634 H486 M442 654 H486" style="stroke-width:1.3"/>
  </g>

  <rect class="placeholder" x="175" y="690" width="50" height="113" rx="14" role="img" aria-label="Hand pointing at the start of the road"/>

  <!-- benefits chart -->
  <g class="chart">
    <path class="chart-axis" d="M800 578 V668 H960"/>
    <rect class="chart-bar" x="822" y="632" width="8" height="36"/>
    <rect class="chart-bar" x="833" y="622" width="8" height="46"/>
    <rect class="chart-bar" x="846" y="650" width="8" height="18"/>
    <rect class="chart-bar" x="857" y="628" width="8" height="40"/>
    <rect class="chart-bar" x="870" y="612" width="8" height="56"/>
    <rect class="chart-bar" x="881" y="600" width="8" height="68"/>
    <rect class="chart-bar" x="897" y="622" width="8" height="46"/>
    <rect class="chart-bar" x="908" y="608" width="8" height="60"/>
    <rect class="chart-bar" x="928" y="605" width="8" height="63"/>
    <rect class="chart-bar" x="940" y="593" width="8" height="75"/>
  </g>
  <line class="pole" x1="800" y1="682" x2="800" y2="748"/>
  <path class="flag-light" d="M788 693 H950 L930 712 L950 731 H788Z"/>
  <text class="script" x="815" y="720" font-size="22">Benefits</text>

  <!-- step numbers -->
  <g class="steps">
    <circle class="step-ring" cx="162" cy="604" r="30"/><text class="step-number" x="162" y="613" text-anchor="middle" font-size="30">1</text>
    <circle class="step-ring" cx="76" cy="376" r="20"/><text class="step-number" x="76" y="384" text-anchor="middle">2</text>
    <circle class="step-ring" cx="370" cy="404" r="20"/><text class="step-number" x="370" y="412" text-anchor="middle">3</text>
    <circle class="step-ring" cx="538" cy="403" r="20"/><text class="step-number" x="538" y="411" text-anchor="middle">4</text>
    <circle class="step-ring" cx="745" cy="712" r="20"/><text class="step-number" x="745" y="720" text-anchor="middle">5</text>
    <circle class="step-ring" cx="933" cy="353" r="20"/><text class="step-number" x="933" y="361" text-anchor="middle">6</text>
    <circle class="step-ring" cx="601" cy="270" r="20"/><text class="step-number" x="601" y="278" text-anchor="middle">7</text>
    <circle class="step-ring" cx="77" cy="170" r="20"/><text class="step-number" x="77" y="178" text-anchor="middle">9</text>
    <circle class="step-ring" cx="404" cy="67" r="20"/><text class="step-number" x="404" y="75" text-anchor="middle">10</text>
    <circle class="step-ring" cx="980" cy="40" r="20"/><text class="step-number" x="980" y="48" text-anchor="middle">11</text>
  </g>
</svg>
</body>
</html>
```